Veltrano Community Development Planning New web site

Design a new web site. I have a budget of $1,500.00.
Attached on PowerPoint is a complete site plan. Home page and linked pages.
10 - 12 pages. All copy and photos will be supplied. (300dpi)
I have shown them the concept which they like.
No data bases required. Home page with animations dissolving.
They former web site has been taken down. They have been in business 30 years in New Jersey
Colors teal blues and greens
There will be a new logo)being designed)
The text in home page copy will give you a detailed story what they are all about.

files have been approved for Veltrano, Inc.   Tomas is the designer

Industry/Entity Type

Community

```html
<!DOCTYPE html>
<html lang="en">
<head>
<meta charset="utf-8">
<title>Veltrano, Inc. — Community Development Planning</title>
<link href="https://fonts.googleapis.com/css2?family=Open+Sans:wght@400;600;700;800&display=swap" rel="stylesheet">
<style>
:root{
  --brand-blue:#1c56a8;
  --brand-green:#3aa935;
  --green-dark:#2a8a29;
  --heading-teal:#1b6aa5;
  --text:#555;
  --muted:#888;
  --rule:#dcdcdc;
  --panel:#f4f4f4;
  --footer-bg:#1f1f1f;
  --footer-text:#bbb;
  --alert-red:#d9232d;
}
*{box-sizing:border-box;margin:0;padding:0}
html,body{width:820px;height:1200px;overflow:hidden;background:#fff}
body{font-family:"Open Sans",Arial,sans-serif;color:var(--text);font-size:9px;line-height:1.5}
.wrap{width:680px;margin:0 auto;position:relative}
/* header */
.site-header{height:80px}
.site-header .wrap{height:80px;display:flex;justify-content:space-between;align-items:center}
.brand-name{font-size:28px;font-weight:800;color:var(--brand-blue);line-height:1}
.brand-tag{font-size:12px;font-weight:700;color:#333;margin-top:3px}
.phone{display:flex;align-items:center;gap:8px;font-size:20px;font-weight:800;color:var(--brand-blue)}
/* nav */
.main-nav{height:28px;background:var(--brand-green);border-bottom:3px solid var(--green-dark)}
.main-nav ul{list-style:none;display:flex;width:680px;margin:0 auto;height:25px}
.main-nav li{flex:1;text-align:center;color:#fff;font-size:9px;font-weight:600;line-height:25px}
.main-nav li.active{background:var(--green-dark)}
/* hero */
.hero{height:237px;background:linear-gradient(120deg,#e9eef3 0%,#cfd9e2 45%,#f3f4f2 70%,#dfe6ea 100%);position:relative}
.hero-arrow{position:absolute;top:105px;width:18px;height:26px;background:rgba(0,0,0,.25);color:#fff;font-size:14px;text-align:center;line-height:26px}
/* sections */
.section-title{font-size:17px;font-weight:700;color:var(--heading-teal);margin-bottom:8px}
.our-company{height:190px;padding-top:14px}
.our-company .wrap{display:flex;gap:20px}
.our-company .copy{flex:1;font-size:8.5px}
.read-more{color:var(--brand-green);font-weight:600;font-size:8px}
.company-photo{width:200px;height:115px;margin-top:30px;background:linear-gradient(135deg,#c9d3dc,#8fa3b3 60%,#d8c7a8)}
.services{height:190px}
.service-grid{display:flex;gap:14px}
.service-card{flex:1}
.service-card .photo{height:105px;position:relative}
.service-card .photo .badge{position:absolute;right:8px;top:8px;width:18px;height:18px;border-radius:50%;background:var(--brand-green)}
.service-card .caption{background:var(--brand-green);color:#fff;font-size:8.5px;font-weight:700;text-align:center;padding:6px 4px}
.p1{background:linear-gradient(135deg,#2f6c3a,#8bb062)}
.p2{background:linear-gradient(135deg,#3f6f8e,#b09266)}
.p3{background:linear-gradient(135deg,#c9b58a,#5d8a5a)}
/* three columns */
.triple{height:180px}
.triple .wrap{display:flex;gap:22px}
.col{flex:1}
.col h3{font-size:11px;font-weight:700;color:#333;margin-bottom:8px}
.post{display:flex;gap:8px;margin-bottom:10px;font-size:7.5px}
.post .date{width:24px;height:30px;border:1px solid var(--rule);text-align:center;font-size:11px;font-weight:700;color:#333;line-height:1.1;padding-top:3px}
.post .date span{display:block;font-size:6.5px;font-weight:400;color:var(--muted)}
.post b{display:block;font-size:8px;color:#333}
.acc-item{border:1px solid var(--rule);height:16px;margin-bottom:4px;font-size:7.5px;padding:0 6px;line-height:14px;color:#333;position:relative}
.acc-item::after{content:"+";position:absolute;right:6px}
.acc-open{border:1px solid var(--rule);padding:6px;font-size:7.5px;margin-bottom:4px}
.quote{background:var(--panel);padding:8px;font-size:7.5px;position:relative;border-left:3px solid var(--brand-green)}
.quote-author{display:flex;gap:6px;align-items:center;margin-top:8px;font-size:7.5px}
.quote-author i{width:22px;height:22px;background:#c7ccd1;display:block}
/* people */
.people{height:140px}
.people-head{display:flex;justify-content:space-between;align-items:center}
.pager{display:flex;gap:3px}
.pager i{width:12px;height:12px;border:1px solid var(--rule);display:block}
.people-grid{display:flex;gap:30px;margin-top:4px}
.person{flex:1;display:flex;gap:12px;font-size:7.5px}
.person .avatar{width:56px;height:56px;border-radius:50%;background:linear-gradient(135deg,#b7c0c8,#7d8a94);flex:none}
.person .more{text-align:right;color:var(--brand-green);font-weight:600;margin-top:4px}
/* partners */
.partners{height:45px}
.partners .wrap{display:flex;justify-content:space-between;align-items:center;height:45px}
.partner{width:62px;height:20px;background:#d8dde2;border-radius:3px}
/* footer */
.site-footer{height:90px;background:var(--footer-bg);color:var(--footer-text);border-top:4px solid var(--brand-green)}
.site-footer .wrap{display:flex;gap:30px;padding-top:8px}
.f-col h4{color:#fff;font-size:8px;font-weight:700;margin-bottom:3px}
.f-col ul{list-style:none;font-size:7px;line-height:1.45}
.f-col.links{width:110px}
.subscribe{width:170px}
.subscribe .field{height:11px;background:#fff;margin-bottom:4px;font-size:6.5px;color:#999;padding-left:4px;line-height:11px}
.subscribe .btn{width:40px;height:12px;background:var(--alert-red);color:#fff;font-size:7px;text-align:center;line-height:12px}
.social{display:flex;gap:3px;margin-left:auto}
.social i{width:12px;height:12px;background:#4a6a8a;display:block}
.copyright{height:20px;background:#111;color:#888;font-size:7px;text-align:center;line-height:20px}
</style>
</head>
<body>
<header class="site-header">
  <div class="wrap">
    <div class="brand">
      <div class="brand-name">Veltrano, Inc.</div>
      <div class="brand-tag">Community Development Planning</div>
    </div>
    <div class="phone">
      <svg width="20" height="20" viewBox="0 0 24 24"><path fill="#1c56a8" d="M6.6 10.8a15.2 15.2 0 0 0 6.6 6.6l2.2-2.2c.3-.3.7-.4 1-.2 1.1.4 2.3.6 3.6.6.6 0 1 .4 1 1V20c0 .6-.4 1-1 1A17 17 0 0 1 3 4c0-.6.4-1 1-1h3.5c.6 0 1 .4 1 1 0 1.3.2 2.5.6 3.6.1.3 0 .7-.2 1z"/></svg>
      800 555 0142
    </div>
  </div>
</header>
<nav class="main-nav">
  <ul>
    <li class="active">Home</li><li>Our Company</li><li>Services</li><li>Housing Applications</li><li>Affordable Applications</li><li>Contact Us</li>
  </ul>
</nav>
<section class="hero" role="img" aria-label="Drafting table with technical drawing, pencil and eraser">
  <span class="hero-arrow" style="left:0">&#8249;</span>
  <span class="hero-arrow" style="right:0">&#8250;</span>
</section>
<section class="our-company">
  <div class="wrap">
    <div class="copy">
      <h2 class="section-title">Our Company</h2>
      <p>For thirty years our team has helped towns across New Jersey plan stronger neighborhoods. We guide housing programs, renovation projects and local growth plans from first idea to finished work. Our planners listen to residents, study each site and shape practical plans that fit real budgets and real families.</p>
      <p style="margin-top:5px">We manage applications for affordable housing, prepare grant requests, coordinate contractors and report results to councils and funding partners. Every project is built around clear goals, open communication and careful use of public funds, so communities can see lasting change on their own streets.</p>
      <p style="margin-top:5px"><span class="read-more">Read More »</span></p>
    </div>
    <div class="company-photo" role="img" aria-label="Planners in hard hats reviewing plans on a building site"></div>
  </div>
</section>
<section class="services">
  <div class="wrap">
    <h2 class="section-title">Services</h2>
    <div class="service-grid">
      <div class="service-card"><div class="photo p1" role="img" aria-label="Renovated family house"><span class="badge"></span></div><div class="caption">Housing and Renovation</div></div>
      <div class="service-card"><div class="photo p2" role="img" aria-label="Community meeting and local development"><span class="badge"></span></div><div class="caption">Community and Economic Development</div></div>
      <div class="service-card"><div class="photo p3" role="img" aria-label="Grant funding paperwork on a desk"><span class="badge"></span></div><div class="caption">Grants and Funding Opportunities</div></div>
    </div>
  </div>
</section>
<section class="triple">
  <div class="wrap">
    <div class="col">
      <h3>Latest Blog</h3>
      <div class="post"><div class="date">24<span>Feb</span></div><div><b>This is a Standard Post</b>New housing rehabilitation funds open this spring for eligible owners in participating towns. Read more »</div></div>
      <div class="post"><div class="date">23<span>Feb</span></div><div><b>This is a Standard Post</b>Our planners share five simple steps to prepare a strong local grant application. Read more »</div></div>
    </div>
    <div class="col">
      <h3>More about us</h3>
      <div class="acc-item">Who we are</div>
      <div class="acc-open">We are a small planning firm serving towns, counties and nonprofit partners across the state.</div>
      <div class="acc-item">What we do</div>
      <div class="acc-item">Where we work</div>
    </div>
    <div class="col">
      <h3>Testimonials</h3>
      <div class="quote">Their team made a complicated housing program simple for our residents and kept every deadline on track.</div>
      <div class="quote-author"><i></i><div><b style="color:#333">Dana Morrow</b><br>Town Administrator</div></div>
    </div>
  </div>
</section>
<section class="people">
  <div class="wrap">
    <div class="people-head"><h2 class="section-title">Our Peoples</h2><div class="pager"><i></i><i></i></div></div>
    <div class="people-grid">
      <div class="person"><div class="avatar" role="img" aria-label="Team member portrait"></div><div><p>Our senior planner leads housing programs and works closely with local officials to turn community goals into clear, funded plans that residents can trust.</p><p class="more">View details »</p></div></div>
      <div class="person"><div class="avatar" role="img" aria-label="Team member portrait"></div><div><p>Our grants manager prepares funding requests, tracks program budgets and keeps every partner informed from application through final report and closeout.</p><p class="more">View details »</p></div></div>
    </div>
  </div>
</section>
<section class="partners" aria-label="Partners">
  <div class="wrap">
    <span class="partner"></span><span class="partner"></span><span class="partner"></span><span class="partner"></span><span class="partner"></span><span class="partner"></span><span class="partner"></span><span class="partner"></span>
  </div>
</section>
<footer class="site-footer">
  <div class="wrap">
    <div class="f-col links"><h4>Company</h4><ul><li>Home</li><li>Our Company</li><li>Services</li><li>Housing</li><li>Contact Us</li><li>Careers</li></ul></div>
    <div class="f-col links"><h4>Links</h4><ul><li>Home</li><li>News</li><li>Photography</li><li>Publishing</li><li>Technology</li><li>Theatre</li></ul></div>
    <div class="f-col subscribe"><h4>Subscribe</h4><div class="field">Name</div><div class="field">Email</div><div class="btn">Submit</div></div>
    <div class="f-col" style="margin-left:auto"><h4>Follow us</h4><div class="social"><i></i><i></i><i></i><i></i><i></i></div></div>
  </div>
</footer>
<div class="copyright">Copyright Veltrano, All Rights Reserved</div>
</body>
</html>
```